Zielgruppe
Beamer Vermietung
Aufgabenstellung
Erstellung 2 professionell aussehender Webseiten.
Projektor-Verleih-Region-Wendlar.de
sowie
Projektor-Verleih-Region-Haselfurtheim.de
Die Seiten sind aktuell im Betrieb, aber haben ein sehr veraltetes Design.
Die Seiten können ähnlich aussehen, sollten aber etwas unterschiedlich sein, damit sie für den Kunden leicht anders aussehen.
Wichtig ist, dass alle Seiten, inklusive Startseite, Unterseiten und Links designed werden und das dieses Design in die bestehende Wordpress Installation eingepflegt wird.
Es ist also notwendig, gute Wordpress Kenntnisse zu haben um dann auch zwei fertige Wordpress Seiten liefern zu können.

```html
<!DOCTYPE html>
<html lang="de">
<head>
<meta charset="utf-8">
<title>Beamer und Leinwand Vermietung</title>
<link href="https://fonts.googleapis.com/css2?family=Roboto:wght@300;400;500;700&family=Roboto+Condensed:wght@700&display=swap" rel="stylesheet">
<style>
  :root{
    --green:#8cc043;
    --navy:#2c3d5a;
    --navy-deep:#26354f;
    --light:#efefef;
    --topbar:#eeeeee;
    --text:#6b6b6b;
    --grey:#7a7a7a;
    --white:#ffffff;
  }
  *{margin:0;padding:0;box-sizing:border-box}
  html,body{width:1200px;height:2271px;overflow:hidden}
  body{position:relative;background:var(--white);font-family:'Roboto',sans-serif;color:var(--navy)}
  .abs{position:absolute}

  .topbar{left:0;top:0;width:1200px;height:31px;background:var(--topbar);border-bottom:1px solid #dcdcdc}
  .topbar .domain{left:162px;top:9px;font-size:11px;color:#555}
  .social{top:8px;width:15px;height:15px;border-radius:50%;background:var(--navy)}
  .social.active{background:var(--green)}

  .header{left:0;top:31px;width:1200px;height:70px;background:var(--white)}
  .brand{left:159px;top:18px;font-size:25px;color:var(--green);font-weight:400;letter-spacing:-.2px}
  .header-links{right:161px;top:25px;display:flex;gap:18px;font-size:13px;font-weight:500;color:#2a5b9a;align-items:center}
  .header-links svg{margin-right:7px;vertical-align:-3px}

  .nav{left:0;top:101px;width:1200px;height:49px;background:var(--navy)}
  .nav ul{position:absolute;left:161px;top:0;display:flex;list-style:none;height:49px}
  .nav li{color:var(--white);font-size:14px;font-weight:500;line-height:49px;padding:0 10px}
  .nav li.active{background:var(--green);color:var(--navy);padding:0 10px 0 12px}

  .hero{left:0;top:150px;width:1200px;height:458px;background:linear-gradient(100deg,#3b3530 0%,#5e5248 35%,#8a7a6a 55%,#6f7a86 80%,#4a5566 100%)}
  .hero-rule{left:159px;top:256px;width:28px;height:3px;background:var(--white)}
  .hero-title{left:159px;top:262px;font-size:46px;font-weight:700;color:var(--white);line-height:55px}
  .hero-sub{left:160px;top:374px;font-size:25px;font-weight:500;color:var(--white)}
  .btn{left:161px;top:464px;width:141px;height:36px;border-radius:18px;background:var(--green);color:var(--navy);font-size:14px;font-weight:700;text-align:center;line-height:36px}

  .strip{left:0;top:608px;width:1200px;height:84px;background:var(--light)}
  .strip-text{left:179px;top:634px;font-family:'Roboto Condensed',sans-serif;font-weight:700;font-size:29px;color:var(--navy);white-space:nowrap}
  .price{display:inline-block;width:60px;height:60px;border-radius:50%;background:var(--green);text-align:center;line-height:60px;margin:-16px 2px}

  .center{left:0;width:1200px;text-align:center}
  .lead{top:722px;font-size:31px;font-weight:300;line-height:37px}
  .headline{top:847px;font-size:35px;font-weight:700}
  .headline-sub{top:888px;font-size:21px;font-weight:300;color:var(--grey)}
  .domain-title{top:1190px;font-size:37px;font-weight:300}
  .domain-sub{top:1234px;font-size:28px;font-weight:300;color:var(--grey)}
  .domain-claim{top:1280px;font-size:30px;font-weight:500}

  .photo{border-radius:4px}

  .copy{width:412px;font-size:15px;line-height:22.5px;color:var(--text);text-align:justify;font-weight:300}
  .copy p{margin-bottom:22.5px}

  .booking{left:0;top:2052px;width:1200px;height:168px;background:linear-gradient(115deg,var(--navy) 0%,#34476a 40%,var(--navy-deep) 70%,#31436a 100%)}
  .booking-title{left:158px;top:2113px;font-size:44px;font-weight:500;color:var(--green)}
  .booking-tel{right:161px;top:2118px;font-size:35px;font-weight:300;color:var(--white);display:flex;align-items:center;gap:18px}

  .footer{left:0;top:2220px;width:1200px;height:51px;background:var(--green);text-align:center;font-size:12px;line-height:51px;color:var(--navy)}
</style>
</head>
<body>

<div class="abs topbar">
  <div class="abs domain">projektor-verleih-region-haselfurtheim.de</div>
  <div class="abs social active" style="left:926px"></div>
  <div class="abs social" style="left:956px"></div>
  <div class="abs social" style="left:985px"></div>
  <div class="abs social" style="left:1015px"></div>
</div>

<header class="abs header">
  <div class="abs brand">Beamer und Leinwand Vermietung</div>
  <div class="abs header-links">
    <span><svg width="20" height="13" viewBox="0 0 20 13"><rect x="0.75" y="0.75" width="18.5" height="11.5" fill="none" stroke="#2c3d5a" stroke-width="1.3"/><path d="M1 1 L10 7.5 L19 1" fill="none" stroke="#2c3d5a" stroke-width="1.3"/></svg>Kontakt / Anreise</span>
    <span>Impressum</span>
  </div>
</header>

<nav class="abs nav">
  <ul>
    <li class="active">Beamer mieten</li>
    <li>HD Beamer mieten</li>
    <li>Full-HD Beamer mieten</li>
    <li>Reservieren oder Buchen</li>
    <li>Preisliste</li>
    <li>Datenschutzerklärung</li>
  </ul>
</nav>

<section class="abs hero" role="img" aria-label="Foto: Projektor auf einem Tisch in einem Besprechungsraum"></section>
<div class="abs hero-rule"></div>
<h1 class="abs hero-title">Beamer mieten<br>in Haselfurtheim</h1>
<div class="abs hero-sub">NEU: Jetzt auch HD-Beamer!</div>
<div class="abs btn">KONTAKT</div>

<section class="abs strip">
  <svg class="abs" style="left:112px;top:18px" width="50" height="40" viewBox="0 0 50 40"><circle cx="16" cy="24" r="12" fill="#8cc043"/><circle cx="41.5" cy="6" r="5" fill="#2c3d5a"/></svg>
</section>
<div class="abs strip-text">Projektoren und Leinwände ab bereits <span class="price">30€</span> pro Tag</div>

<h2 class="abs center lead">Sie möchten einen Beamer im Kreis<br>Haselfurtheim oder Umgebung mieten?</h2>
<h2 class="abs center headline">! Beamer mieten zu TOP-Konditionen !</h2>
<div class="abs center headline-sub">NEU: Jetzt auch HD- und Business FULL-HD-Projektoren</div>

<div class="abs photo" style="left:161px;top:987px;width:274px;height:150px;background:linear-gradient(160deg,#4a4a4a,#1e1e1e 70%,#e6e6e6)" role="img" aria-label="Produktfoto: schwarzer Projektor"></div>
<div class="abs photo" style="left:474px;top:999px;width:269px;height:148px;background:linear-gradient(160deg,#f6f6f6,#d8d8d8 70%,#f0f0f0)" role="img" aria-label="Produktfoto: weißer Projektor"></div>
<div class="abs photo" style="left:785px;top:995px;width:254px;height:132px;background:linear-gradient(170deg,#3a3a3a,#9a948c 45%,#2a2a2a)" role="img" aria-label="Produktfoto: grau-schwarzer Projektor"></div>

<h2 class="abs center domain-title">Projektor-Verleih-Region-Haselfurtheim.de –</h2>
<div class="abs center domain-sub">Ihre Adresse für</div>
<h3 class="abs center domain-claim">Projektor-Vermietung und Leinwand Anmietung!</h3>

<div class="abs photo" style="left:212px;top:1371px;width:359px;height:295px;background:radial-gradient(ellipse at 50% 45%,#5b5b60 0%,#8a8a90 40%,#ffffff 75%)" role="img" aria-label="Produktfoto: Projektor mit Fernbedienung"></div>
<div class="abs photo" style="left:660px;top:1381px;width:343px;height:225px;background:radial-gradient(ellipse at 55% 40%,#b8bcc6 0%,#d4d7de 45%,#ffffff 75%)" role="img" aria-label="Produktfoto: silberner Projektor mit Fernbedienung"></div>

<div class="abs copy" style="left:160px;top:1711px">
  <p>Zu unseren Miet-Geräten können optional auch passende Leinwände zu Ihrem gewünschten Projektor hinzugebucht werden. Unsere Projektoren und Leinwände gibt es bereits ab günstigen 30€ pro Tag. Alle Preise können Sie unserer Preisliste entnehmen.</p>
  <p>Unser Sortiment erstreckt sich von Heim-Projektoren für den privaten Bedarf über HD-fähige Geräte bis hin zu Business Full-HD-Geräten, die für großräumige Geschäftspräsentationen sowie für Full-HD TV Übertragungen geeignet sind. Somit haben Sie das perfekte Klang- und Bilderlebnis für Ihre Präsentation oder Ihr Event.</p>
</div>
<div class="abs copy" style="left:625px;top:1711px">
  <p>Wir bieten Ihnen die Möglichkeit, auch über Wochenenden zu vergünstigten Wochenend-Tarifen zu bestellen. Falls Sie Fragen zu dem Ablauf, zu den Projektoren oder zu dem Mietvorgang haben, können Sie uns jederzeit kontaktieren, wir helfen Ihnen gerne weiter!</p>
  <p>Sie kommen aus der Region Wendlar? Unsere aktuellen Angebote hierfür finden Sie unter https://www.projektor-verleih-region-wendlar.de</p>
  <p>Bei Fragen zur Anfahrt können Sie unseren Anfahrt-Navigator unter „Kontakt / Anreise“ nutzen.</p>
</div>

<section class="abs booking"></section>
<div class="abs booking-title">Reservieren oder Buchen</div>
<div class="abs booking-tel">
  <svg width="34" height="26" viewBox="0 0 34 26"><path d="M2 9 C2 3 32 3 32 9 L32 12 L24 12 L24 8 L10 8 L10 12 L2 12 Z" fill="#8cc043"/><path d="M9 13 L25 13 L30 24 L4 24 Z" fill="#8cc043"/><circle cx="17" cy="18.5" r="3.2" fill="#2c3d5a"/></svg>
  <span>Tel: 0160 / 4829175</span>
</div>

<footer class="abs footer">Copyright © 2020.&nbsp; Projektor-Verleih-Region-Wendlar.de</footer>

</body>
</html>
```